Soap Company Looking To Design New Soap Scent Boxes

we are looking to create a soap box similar to pa grunwell. we would like the circle cut out on the top right corner of the box. we are looking for a design that will allow us to use different color base banners for different soap scents (like pa. grunwell). we want the soap name scents to be large and readable on the bottom banner (like pa.grunwell). we have included our brand figure (logo) and some previous older soap box designs that we were making before the brand figure. the box dims are attached.

```html
<!DOCTYPE html>
<html lang="en">
<head>
<meta charset="utf-8">
<title>Plumeria Soap Box – Dieline</title>
<link rel="stylesheet" href="https://fonts.googleapis.com/css2?family=Cinzel:wght@400;600;700&family=Montserrat:wght@400;500;600&display=swap">
<style>
  :root {
    --canvas-bg: #eef1f3;
    --kraft: #dcb793;
    --kraft-dark: #cfa982;
    --scent-red: #c8244a;
    --ink: #3a2a1e;
    --paper-white: #ffffff;
    --cut-line: #5aa7d8;
    --fold-line: #e0505a;
    --safe-line: #3fae6a;
    --brand-gold: #f0b43c;
  }
  html, body {
    margin: 0;
    width: 693px;
    height: 1200px;
    overflow: hidden;
    background: var(--canvas-bg);
  }
  .canvas {
    position: relative;
    width: 693px;
    height: 1200px;
    display: flex;
    align-items: center;
    justify-content: center;
  }
  .dieline { width: 693px; height: 497px; display: block; }
  .kraft { fill: var(--kraft); stroke: var(--cut-line); stroke-width: 1; }
  .scent-band { fill: var(--scent-red); }
  .fold { fill: none; stroke: var(--fold-line); stroke-width: 0.7; }
  .safe { fill: none; stroke: var(--safe-line); stroke-width: 0.7; }
  .cutout { fill: var(--paper-white); }
  .serif { font-family: "Cinzel", serif; }
  .sans { font-family: "Montserrat", sans-serif; }
  .title-white { fill: var(--paper-white); font-family: "Cinzel", serif; font-weight: 600; }
  .label-white { fill: var(--paper-white); font-family: "Montserrat", sans-serif; letter-spacing: 0.5px; }
  .ink-text { fill: var(--ink); }
  .icon { fill: none; stroke: var(--paper-white); stroke-width: 1.2; stroke-linejoin: round; stroke-linecap: round; }
  .brand-mark { fill: var(--brand-gold); }
</style>
</head>
<body>
<main class="canvas">
  <svg class="dieline" viewBox="30 1030 935 670" xmlns="http://www.w3.org/2000/svg" aria-label="Plumeria soap box dieline">

    <!-- lid tuck flap -->
    <path class="kraft" d="M85 1098 L85 1060 Q85 1036 110 1036 L385 1036 Q410 1036 410 1060 L410 1098 Z"/>
    <rect class="safe" x="110" y="1060" width="280" height="25" rx="6"/>

    <!-- lid panel -->
    <rect class="kraft" x="98" y="1098" width="312" height="112"/>
    <rect class="scent-band" x="110" y="1110" width="286" height="85"/>
    <g transform="rotate(180 253 1150)">
      <text class="title-white" x="253" y="1142" font-size="28" text-anchor="middle">PLUMERIA</text>
      <text class="label-white" x="253" y="1162" font-size="8" text-anchor="middle">COLD PRESSED ARTISAN SOAP</text>
    </g>

    <!-- glue flap -->
    <path class="kraft" d="M98 1210 L35 1215 L35 1525 L98 1530 Z"/>
    <rect class="safe" x="60" y="1230" width="24" height="270"/>

    <!-- back panel -->
    <rect class="kraft" x="98" y="1210" width="312" height="320"/>

    <!-- side panel + flaps -->
    <path class="kraft" d="M420 1210 L420 1135 Q420 1125 430 1125 L508 1130 Q520 1132 520 1145 L520 1210 Z"/>
    <rect class="kraft" x="410" y="1210" width="110" height="320"/>
    <path class="kraft" d="M420 1530 L510 1530 L510 1600 Q510 1610 500 1610 L430 1610 Q420 1610 420 1600 Z"/>

    <!-- front panel + bottom flap -->
    <rect class="kraft" x="520" y="1210" width="315" height="320"/>
    <path class="kraft" d="M510 1530 L845 1530 L845 1665 Q845 1695 815 1695 L540 1695 Q510 1695 510 1665 Z"/>
    <rect class="safe" x="535" y="1640" width="285" height="30" rx="6"/>
    <rect class="fold" x="530" y="1620" width="295" height="4"/>

    <!-- right side panel + flaps -->
    <path class="kraft" d="M835 1210 L835 1145 Q835 1125 850 1125 L945 1130 Q958 1132 958 1145 L958 1210 Z"/>
    <rect class="kraft" x="835" y="1210" width="123" height="320"/>
    <path class="kraft" d="M845 1530 L950 1530 L950 1600 Q950 1610 940 1610 L855 1610 Q845 1610 845 1600 Z"/>

    <!-- fold lines -->
    <line class="fold" x1="98" y1="1210" x2="958" y2="1210"/>
    <line class="fold" x1="35" y1="1525" x2="958" y2="1525"/>
    <line class="fold" x1="410" y1="1210" x2="410" y2="1530"/>
    <line class="fold" x1="520" y1="1210" x2="520" y2="1530"/>
    <line class="fold" x1="835" y1="1210" x2="835" y2="1530"/>

    <!-- scent banner band across back + side -->
    <rect class="scent-band" x="35" y="1422" width="490" height="73"/>

    <!-- back panel copy -->
    <g class="back-copy">
      <rect class="safe" x="110" y="1222" width="286" height="285"/>
      <text class="serif ink-text" x="253" y="1255" font-size="12" letter-spacing="5" text-anchor="middle">HOUR OF THYME</text>
      <text class="serif ink-text" x="253" y="1285" font-size="15" font-weight="600" text-anchor="middle">ARTISAN SOAP BAR</text>
      <g class="sans ink-text" font-size="8" text-anchor="middle">
        <text x="253" y="1327">OUR BATH SOAPS COLLECTION ARE INFUSED WITH</text>
        <text x="253" y="1338">ALL-ORGANIC INGREDIENTS, INCLUDING COCONUT OIL, CANOLA</text>
        <text x="253" y="1349">OIL, SOYBEAN OIL, SHEA BUTTER, WATER, SODIUM HYDROXIDE</text>
        <text x="253" y="1360">(LYE) OLIVE POMACE OIL, SUNFLOWER OIL, FRAGRANCE.</text>
        <text x="253" y="1384" font-weight="600">THIS IS NATURE IN A BAR!</text>
      </g>
    </g>

    <!-- feature icons -->
    <g class="features">
      <line x1="205" y1="1432" x2="205" y2="1488" stroke="#d9506f" stroke-width="0.8"/>
      <line x1="302" y1="1432" x2="302" y2="1488" stroke="#d9506f" stroke-width="0.8"/>
      <path class="icon" d="M148 1458 L148 1442 M152 1456 L152 1438 M156 1456 L156 1439 M160 1458 L160 1442 M146 1452 L146 1462 Q154 1468 162 1462 L162 1448"/>
      <text class="label-white" x="156" y="1474" font-size="7" text-anchor="middle">HANDMADE</text>
      <path class="icon" d="M253 1440 Q246 1448 253 1457 Q260 1448 253 1440 Z M253 1457 Q242 1456 241 1445 M253 1457 Q264 1456 265 1445 M243 1458 L263 1458"/>
      <text class="label-white" x="253" y="1474" font-size="7" text-anchor="middle">ALL NATURAL</text>
      <text class="label-white" x="253" y="1483" font-size="7" text-anchor="middle">INGREDIENTS</text>
      <rect class="icon" x="342" y="1440" width="13" height="18" rx="3"/>
      <circle class="icon" cx="345" cy="1438" r="2.5"/>
      <text class="label-white" x="349" y="1474" font-size="7" text-anchor="middle">VARIETY OF</text>
      <text class="label-white" x="349" y="1483" font-size="7" text-anchor="middle">SOAP SCENT</text>
    </g>

    <!-- side panel: scent list -->
    <g class="scent-list">
      <rect class="safe" x="420" y="1222" width="90" height="285"/>
      <rect class="scent-band" x="422" y="1224" width="86" height="14"/>
      <text class="label-white" x="465" y="1234" font-size="7" font-weight="600" text-anchor="middle">AVAILABLE SCENTS</text>
      <g class="sans ink-text" font-size="6.8" text-anchor="middle">
        <text x="465" y="1251">Cedarwood Tea Tree</text>
        <text x="465" y="1261">Charcoal Aloe</text>
        <text x="465" y="1271">Cool Water</text>
        <text x="465" y="1281">Dead Sea Scrub</text>
        <text x="465" y="1291">Eucalyptus Aloe</text>
        <text x="465" y="1301">Hydrangea</text>
        <text x="465" y="1311">Jasmine Lime Scrub</text>
        <text x="465" y="1321">Mango Papaya</text>
        <text x="465" y="1331">Mountain Air</text>
        <text x="465" y="1341">Nag Champa</text>
        <text x="465" y="1351">Plumeria</text>
        <text x="465" y="1361">Pomegranate Cherry</text>
        <text x="465" y="1371">Raspberry Rush</text>
        <text x="465" y="1381">Raspberry Vanilla</text>
        <text x="465" y="1391">Sandalwood Rose</text>
        <text x="465" y="1401">Tangerine Grapefruit</text>
        <text x="465" y="1411">Wild Passion</text>
        <text x="465" y="1421">Wildflowers</text>
      </g>
      <text class="title-white" x="465" y="1461" font-size="9" text-anchor="middle">PLUMERIA</text>
    </g>

    <!-- front panel -->
    <g class="front">
      <rect class="safe" x="532" y="1222" width="290" height="285"/>
      <circle class="cutout" cx="788" cy="1253" r="31"/>
      <circle class="brand-mark" cx="640" cy="1330" r="12"/>
      <text class="serif ink-text" x="662" y="1322" font-size="15" font-weight="700">HOUR OF</text>
      <text class="serif ink-text" x="662" y="1346" font-size="22" font-weight="700">THYME</text>
      <path class="scent-band" d="M535 1422 L788 1422 Q808 1422 808 1442 L808 1495 L535 1495 Z"/>
      <text class="title-white" x="677" y="1463" font-size="32" text-anchor="middle">PLUMERIA</text>
      <text class="label-white" x="677" y="1481" font-size="9" text-anchor="middle">COLD PRESSED ARTISAN SOAP</text>
      <text class="sans ink-text" x="677" y="1508" font-size="7" text-anchor="middle">NET WT. 5OZ (140G)</text>
    </g>

    <!-- right side panel -->
    <g class="right-side">
      <rect class="safe" x="845" y="1222" width="90" height="285"/>
      <g transform="rotate(-90 890 1365)" class="sans ink-text" text-anchor="middle" font-size="11" letter-spacing="1.5">
        <text x="890" y="1360">REJUVENATE YOUR</text>
        <text x="890" y="1376">MIND, BODY &amp; SOUL</text>
      </g>
    </g>
  </svg>
</main>
</body>
</html>
```